Ridgely Forge business card for handing simple contact information and generating service awareness

Utilizing the attached logo(s), generate a professional, but approachable, card conveying a sense of capability and integrity. Please only use one logo of the four attached; the different colors are all acceptable, but preference will be given to a design integrating a teal/turquoise logo,

I do not know where to put in the contact information or details?

Target Market(s)

Agriculture, Farming, Timber, Forestry, Construction, Crane Service

Industry/Entity Type

Contact Information for Business Card

Name, Phone Number, email address

Colors

Designer to choose colors to be used in the design.

Requirements
Nice to have
• It would be great to have either a mountain or one of the attached cranes as a backdrop on the rear of the card. Simple watermarks and/or Debossing is also great

```html
<!DOCTYPE html>
<html lang="en">
<head>
<meta charset="utf-8">
<title>Ridgely Forge Business Card</title>
<link rel="stylesheet" href="https://fonts.googleapis.com/css2?family=Montserrat:wght@700;800&family=Lato:wght@400;700&display=swap">
<style>
  :root {
    --teal: #276b5f;
    --teal-light: #3aa394;
    --ink: #1e1f1f;
    --text: #454a49;
    --paper: #ffffff;
    --mist: #e6eeec;
    --backdrop: #d8dcdb;
  }
  * { margin: 0; padding: 0; box-sizing: border-box; }
  html, body { width: 1200px; height: 982px; overflow: hidden; background: var(--backdrop); }
  .stage { position: relative; width: 1200px; height: 982px; }
  .card {
    position: absolute; left: 220px; width: 760px; height: 434px;
    border-radius: 26px; overflow: hidden;
    border: 2px solid var(--teal-light);
    box-shadow: 0 10px 30px rgba(0,0,0,0.18);
  }
  .card-back { top: 34px; background: var(--ink); display: flex; align-items: center; justify-content: center; }
  .back-wordmark {
    font-family: "Montserrat", sans-serif; font-weight: 800; font-size: 58px;
    letter-spacing: 1px; color: var(--teal); text-transform: uppercase;
  }
  .card-front { top: 514px; background: var(--paper); }
  .front-band { position: absolute; inset: 0; width: 100%; height: 100%; }
  .front-wordmark {
    position: absolute; left: 44px; top: 168px;
    font-family: "Montserrat", sans-serif; font-weight: 800; font-size: 34px;
    line-height: 40px;
    color: var(--teal); text-transform: uppercase; letter-spacing: 0.5px;
  }
  .person { position: absolute; right: 48px; top: 70px; text-align: right; color: var(--paper); }
  .person-name { font-family: "Montserrat", sans-serif; font-weight: 700; font-size: 32px; letter-spacing: 0.5px; }
  .person-role { font-family: "Lato", sans-serif; font-size: 21px; margin-top: 2px; }
  .contact-list { position: absolute; left: 44px; top: 232px; list-style: none; font-family: "Lato", sans-serif; font-size: 20px; color: var(--text); }
  .contact-list li { display: flex; align-items: center; gap: 12px; height: 34px; }
  .contact-list svg { width: 18px; height: 18px; fill: var(--teal); flex: none; }
  .divider { position: absolute; left: 318px; top: 238px; width: 2px; height: 122px; background: var(--teal); }
  .address { position: absolute; left: 344px; top: 234px; font-family: "Lato", sans-serif; font-size: 20px; line-height: 31px; color: var(--text); }
  .address .company { color: var(--teal); font-weight: 700; }
</style>
</head>
<body>
<main class="stage">
  <section class="card card-back" aria-label="Card back">
    <div class="back-wordmark">Ridgely Forge</div>
  </section>

  <section class="card card-front" aria-label="Card front">
    <svg class="front-band" viewBox="0 0 760 434" preserveAspectRatio="none" aria-hidden="true">
      <defs>
        <linearGradient id="mist-fade" x1="0" y1="0" x2="1" y2="0">
          <stop offset="0" stop-color="#ffffff" stop-opacity="0"/>
          <stop offset="1" stop-color="#e6eeec"/>
        </linearGradient>
      </defs>
      <polygon points="0,0 760,0 760,225 0,96" fill="#276b5f"/>
      <polygon points="380,161 760,225 760,434 380,434" fill="url(#mist-fade)"/>
    </svg>

    <div class="front-wordmark">Ridgely Forge</div>

    <div class="person">
      <div class="person-name">DANIEL HART</div>
      <div class="person-role">Founder &amp; CEO</div>
    </div>

    <ul class="contact-list">
      <li><svg viewBox="0 0 24 24"><path d="M6.6 10.8a15 15 0 0 0 6.6 6.6l2.2-2.2a1 1 0 0 1 1-.25 11.4 11.4 0 0 0 3.6.57 1 1 0 0 1 1 1V20a1 1 0 0 1-1 1A17 17 0 0 1 3 4a1 1 0 0 1 1-1h3.5a1 1 0 0 1 1 1c0 1.25.2 2.45.57 3.57a1 1 0 0 1-.25 1z"/></svg>(555) 214-3086</li>
      <li><svg viewBox="0 0 24 24"><path d="M7 1h10a2 2 0 0 1 2 2v18a2 2 0 0 1-2 2H7a2 2 0 0 1-2-2V3a2 2 0 0 1 2-2zm0 3v14h10V4zm5 15.5a1 1 0 1 0 0 2 1 1 0 0 0 0-2z"/></svg>(555) 214-3087</li>
      <li><svg viewBox="0 0 24 24"><path d="M6 2h12v5H6zM4 8h16a2 2 0 0 1 2 2v7h-4v5H6v-5H2v-7a2 2 0 0 1 2-2zm4 7v5h8v-5z"/></svg>(555) 214-3088</li>
      <li><svg viewBox="0 0 24 24"><path d="M2 5h20v14H2zm2 2v.5l8 5 8-5V7l-8 5z"/></svg>info@ridgelyforge.com</li>
    </ul>

    <div class="divider"></div>

    <div class="address">
      <div class="company">Ridgely Forge Group</div>
      <div>4780 Alder Creek Road</div>
      <div>Millbrook, VT 05601</div>
      <div>www.ridgelyforge.com</div>
    </div>
  </section>
</main>
</body>
</html>
```